Natural Skincare Product Labels Design

We are looking for a designer to create elegant but quirky, functional product labels for our natural skincare range.
The labels must reflect our brand’s values of simplicity, luxury, and the natural, handmade essence of our products.
https://www.pictogrove.com/marvellaskincare
1. Key Details
Packaging Dimensions
Container Types: Transparent jars.
Sizes for Body Products:
Diameter: 64mm–68mm.
Heights: 80mm, 88mm, and 97mm (lid height: 15mm).
Sizes for Face Creams:
Diameter: 60mm.
Height: 50mm (lid height: 15mm).
Label Fit: For body products, ideally one label size to fit all jar sizes.
For the smaller face cream jars, a separate, tailored label is required.
2. Label Placement
Options include a wrapped-around label or a combination of wrapped-around and top-of-jar elements.
Transparent jars mean the label must leave space for the product to be visible (e.g., partial wrap or cutout areas).
3. Content Requirements
Product Name: Prominently displayed.
Ingredient List: Dedicated space required.
Disclaimer/Usage Instructions: Include space for this information.
4. Design Goals
Look & Feel: Simple, upmarket, and natural, with a handmade essence.
Logo Usage: Our logo is finalized and available in gold, black, and white variants. Use Josefin Bold font for the logo if adjustments are required.
Color Palette: Neutral tones (e.g., whites, blacks, golds) are preferred, with flexibility for subtle pops of color tied to each product’s main ingredient.
5. Imagery
Open to including images and colours (e.g., botanical illustrations) that highlight the main ingredient (e.g., coffee beans, turmeric root, or honeycomb). Also open to labels having a prominent colour to tie it in to the main ingredient.
Alternatively, no images can also work for a clean design.
6. Current Design Context
Our temporary design features gold leaf on top and a simple handmade side label. We’re seeking to elevate this to a more polished, cohesive design.
7. Product Line
- Body Products (Larger Jars)
Tolo Body Butter
Key Ingredients: Guarana & Cupuaçu butter (inspired by Brazil).
Note: “Tolo” is slang for “bum.”
Manuka Honey Body Butter
Key Ingredients: Manuka honey (from New Zealand) & Cupuaçu butter.
Coffee Body Scrub
Key Ingredients: Coffee and Demerara sugar.
Whipped Body Soap - Turmeric
Key Ingredients: Turmeric and Bentonite clay.
Whipped Body Soap - Banana
- Face Products (Smaller Jars)
Face Cream
Key Ingredients: Carrot Oil and Raspberry Oil.
Features natural UV protection.
Good Night Cream
Key Ingredients: Enriched with Magnesium.
Promotes relaxation and restful sleep.
8. Submission Guidelines
Flexibility: Design should allow for consistent branding across all products while accommodating the varying jar sizes and ingredient focus.
Material Considerations: Labels should complement the transparent jars and allow the product inside to remain partially visible.
Print Elements: Incorporating gold accents is a plus but should not overpower the design.
We’re excited to see your vision for a label that celebrates the natural beauty and high quality of our skincare range. Please include mockups to showcase the design in use, particularly on transparent jars of varying sizes.
women 20-50 years of age

```html
<!DOCTYPE html>
<html lang="en">
<head>
<meta charset="utf-8">
<title>Marvella Natural Skincare – Product Labels</title>
<link href="https://fonts.googleapis.com/css2?family=Josefin+Sans:wght@400;600&family=Lora:wght@400;600&display=swap" rel="stylesheet">
<style>
  :root{
    --bg:#ededed;
    --paper:#fbfbf9;
    --ink:#3a3a3a;
    --muted:#8a8a8a;
    --gold:#c9962b;
    --lid:#1d1d1f;
    --tolo:#7b5a8e;
    --manuka:#e08a2e;
    --coffee:#5b4333;
  }
  *{margin:0;padding:0;box-sizing:border-box}
  html,body{width:1200px;height:900px;overflow:hidden;background:var(--bg)}
  .canvas{position:relative;width:1200px;height:900px}

  /* lid label */
  .lid-label{position:absolute;left:460px;top:60px;width:280px;height:280px;border-radius:50%;
    background:var(--lid);display:flex;flex-direction:column;align-items:center;justify-content:center}
  .lid-label .ring{position:absolute;inset:22px;border:1.5px solid var(--gold);border-radius:50%}
  .lid-label .ring-inner{position:absolute;inset:70px;border:1.5px solid var(--gold);border-radius:50%}
  .lid-brand{font-family:"Josefin Sans",sans-serif;font-weight:600;color:var(--gold);font-size:26px;letter-spacing:4px}
  .lid-tag{font-family:"Josefin Sans",sans-serif;font-weight:400;color:var(--gold);font-size:11px;letter-spacing:3px;margin-top:6px}

  /* side labels */
  .label-row{position:absolute;left:30px;top:450px;display:flex;gap:30px}
  .side-label{width:360px;height:250px;display:flex;background:var(--paper);border-radius:6px;overflow:hidden;
    box-shadow:0 1px 3px rgba(0,0,0,.08)}
  .front-panel{width:270px;display:flex;flex-direction:column;position:relative}
  .brand-lockup{display:flex;align-items:center;gap:10px;padding:30px 0 0 32px}
  .brand-dot{width:14px;height:14px;border:1.5px solid var(--gold);border-radius:50%}
  .brand-name{font-family:"Josefin Sans",sans-serif;font-weight:600;color:var(--gold);font-size:18px;letter-spacing:3px;line-height:1}
  .brand-tag{font-family:"Josefin Sans",sans-serif;color:var(--gold);font-size:9px;letter-spacing:2px;padding:4px 0 0 56px}
  .product-name{font-family:"Lora",serif;font-weight:600;font-size:24px;line-height:1.1;padding:22px 22px 0 28px;letter-spacing:-.3px}
  .product-sub{font-family:"Lora",serif;font-size:9px;color:var(--muted);padding:5px 22px 0 28px;line-height:1.3}
  .volume-band{position:absolute;left:0;right:0;bottom:0;height:44px;display:flex;align-items:center;justify-content:center;
    font-family:"Lora",serif;font-size:12px;color:#fff}
  .info-panel{width:90px;border-left:1px dashed #d4d4d4;padding:16px 8px;font-family:"Lora",serif;color:#777;font-size:5.5px;line-height:1.35}
  .info-panel h4{font-family:"Josefin Sans",sans-serif;font-weight:600;font-size:5.5px;letter-spacing:.5px;color:#555;margin:6px 0 2px}
  .info-panel h4:first-child{margin-top:0}

  .tolo .product-name{color:var(--tolo)} .tolo .volume-band{background:var(--tolo)}
  .manuka .product-name{color:var(--manuka)} .manuka .volume-band{background:var(--manuka)}
  .coffee .product-name{color:var(--coffee)} .coffee .volume-band{background:var(--coffee)}
</style>
</head>
<body>
<main class="canvas">
  <section class="lid-label">
    <span class="ring"></span>
    <span class="ring-inner"></span>
    <span class="lid-brand">MARVELLA</span>
    <span class="lid-tag">NATURAL SKINCARE</span>
  </section>

  <section class="label-row">
    <article class="side-label tolo">
      <div class="front-panel">
        <div class="brand-lockup"><span class="brand-dot"></span><span class="brand-name">MARVELLA</span></div>
        <div class="brand-tag">NATURAL SKINCARE</div>
        <h2 class="product-name">Tolo Body Butter</h2>
        <p class="product-sub">Guarana &amp; Cupuaçu Butter<br>(Inspired By Brazil)</p>
        <div class="volume-band">200 ml</div>
      </div>
      <div class="info-panel">
        <h4>INGREDIENTS</h4><p>Cupuaçu butter, shea butter, guarana extract, sweet almond oil, vitamin E.</p>
        <h4>APPLICATION</h4><p>Massage gently into clean skin until absorbed.</p>
        <h4>PRODUCT NOTES</h4><p>Handmade in small batches. Store cool and dry.</p>
        <h4>WARNING</h4><p>For external use only. Patch test first.</p>
      </div>
    </article>

    <article class="side-label manuka">
      <div class="front-panel">
        <div class="brand-lockup"><span class="brand-dot"></span><span class="brand-name">MARVELLA</span></div>
        <div class="brand-tag">NATURAL SKINCARE</div>
        <h2 class="product-name">Manuka Honey<br>Body Butter</h2>
        <p class="product-sub">Manuka honey (from New Zealand)<br>&amp; Cupuaçu butter.</p>
        <div class="volume-band">200 ml</div>
      </div>
      <div class="info-panel">
        <h4>INGREDIENTS</h4><p>Cupuaçu butter, manuka honey, shea butter, jojoba oil, vitamin E.</p>
        <h4>APPLICATION</h4><p>Massage gently into clean skin until absorbed.</p>
        <h4>PRODUCT NOTES</h4><p>Handmade in small batches. Store cool and dry.</p>
        <h4>WARNING</h4><p>For external use only. Patch test first.</p>
      </div>
    </article>

    <article class="side-label coffee">
      <div class="front-panel">
        <div class="brand-lockup"><span class="brand-dot"></span><span class="brand-name">MARVELLA</span></div>
        <div class="brand-tag">NATURAL SKINCARE</div>
        <h2 class="product-name">Coffee Body Scrub</h2>
        <p class="product-sub">Coffee and Demerara sugar</p>
        <div class="volume-band">200 ml</div>
      </div>
      <div class="info-panel">
        <h4>INGREDIENTS</h4><p>Coffee grounds, demerara sugar, coconut oil, sweet almond oil, vitamin E.</p>
        <h4>APPLICATION</h4><p>Massage gently into clean skin until absorbed.</p>
        <h4>PRODUCT NOTES</h4><p>Handmade in small batches. Store cool and dry.</p>
        <h4>WARNING</h4><p>For external use only. Patch test first.</p>
      </div>
    </article>
  </section>
</main>
</body>
</html>
```